Global Expert Network Firm needs business card design

We need business card design for a new company based in Seoul, South Korea called 'Corwell Insight Partners'. We recruit industry experts covering all countries and connect our client and recruited expert by phone, face-to-face meetings and etc. We are a global expert network firm that is focused on delivering high-quality experts to our clients throughout the world. Our clients include multinational corporations, global consulting firms, private equity firms, venture capital firms, asset management companies.
We have made new logo and please find attachment.(Please use new logo)
Target Market(s)
Global Consulting Firms, Investment Firms, Private Equity Firms, Venture Capital Firms.
Industry/Entity Type
Recruitment
Contact Information for Business Card
We need two Languages (English and Korean Version).
The front is Korean and the back is English version.
[The back] [English]
Company Name: Corwell Insight Partners, Inc.
CEO Name: Daniel Park
Address: #507, Hanbit Bldg, 82 Maebongsan-ro, Dobong-gu, Seoul, 01327, Korea
Tel. +82 2 718 4052
Fax. +82 2 864 1097
Mobile. +82 10 7264 8815
Email: daniel@corwellip.com
Web: www.corwellip.com
[The front] [Korean] => Described in same order as English version.
회사명: 코웰인사이트파트너스(주)
대표이사: 박도현
주소: 서울시 도봉구 매봉산로 82 한빛빌딩 507호
Tel. 02 718 4052
Fax. 02 864 1097
Mobile. 010 7264 8815
Web: www.corwellip.com
Look and feel
Each slider illustrates characteristics of the customer's brand and the style your logo design should communicate.

```html
<!DOCTYPE html>
<html lang="en">
<head>
<meta charset="utf-8">
<title>Corwell Insight Partners — Business Card</title>
<link rel="stylesheet" href="https://fonts.googleapis.com/css2?family=Roboto:wght@300;400&family=Noto+Sans+KR:wght@400&family=Marcellus&display=swap">
<style>
  :root {
    --navy: #14214b;
    --navy-text: #1b2656;
    --paper: #f3f3f3;
    --backdrop: #c9c9c9;
    --band-grey: #5a5a5a;
    --cream: #e9e6df;
  }
  * { margin: 0; padding: 0; box-sizing: border-box; }
  html, body { width: 1200px; height: 576px; overflow: hidden; }
  body {
    background: var(--backdrop);
    font-family: "Roboto", "Noto Sans KR", sans-serif;
    position: relative;
  }
  .card {
    position: absolute;
    top: 138px;
    width: 484px;
    height: 292px;
    border-radius: 14px;
    overflow: hidden;
  }
  /* Front */
  .card-front { left: 82px; background: var(--navy); color: var(--cream); }
  .front-wordmark {
    position: absolute; left: 0; right: 0; top: 63px;
    text-align: center;
    font-weight: 300;
    font-size: 38px;
    line-height: 51px;
    letter-spacing: 1px;
  }
  .front-tagline {
    position: absolute; left: 0; right: 0; top: 266px;
    text-align: center;
    font-family: "Marcellus", serif;
    font-size: 8px;
    line-height: 12px;
    letter-spacing: 3px;
  }
  /* Back */
  .card-back { left: 602px; background: var(--paper); color: var(--navy-text); }
  .edge-dot {
    position: absolute; left: -16px; top: 45px;
    width: 28px; height: 50px; border-radius: 50%;
    background: var(--navy);
  }
  .person-name { position: absolute; left: 20px; top: 49px; font-size: 17.5px; line-height: 22px; }
  .person-name .ko { font-family: "Noto Sans KR", sans-serif; font-size: 15px; }
  .person-title { position: absolute; left: 20px; top: 73px; font-size: 10.5px; line-height: 14px; }
  .person-title .ko { font-family: "Noto Sans KR", sans-serif; font-size: 8.5px; margin-left: 4px; }
  .back-wordmark {
    position: absolute; right: 20px; top: 29px;
    text-align: right;
    font-weight: 300;
    font-size: 26px;
    line-height: 34px;
    letter-spacing: .5px;
  }
  .company-en { position: absolute; left: 20px; top: 142px; font-size: 16px; line-height: 20px; }
  .company-ko-row {
    position: absolute; left: 20px; right: 20px; top: 164px;
    display: flex; align-items: flex-end; gap: 8px;
  }
  .company-ko {
    font-family: "Noto Sans KR", sans-serif; font-size: 13.5px; line-height: 20px;
    white-space: nowrap;
  }
  .company-rule { flex: 1; height: 1px; background: var(--navy-text); margin-bottom: 3px; }
  .contacts { position: absolute; left: 20px; top: 201px; font-size: 11px; line-height: 14px; }
  .contact-row { display: flex; gap: 12px; }
  .contact-item { display: flex; align-items: center; gap: 8px; }
  .contact-item svg { width: 9px; height: 9px; fill: var(--navy-text); }
  .address { position: absolute; left: 19px; top: 237px; font-size: 11px; line-height: 14px; }
  .address-ko {
    position: absolute; left: 19px; top: 254px;
    font-family: "Noto Sans KR", sans-serif; font-size: 9px; line-height: 13px;
  }
  .footer-band { position: absolute; left: 0; bottom: 0; width: 484px; height: 14px; }
  .back-tagline {
    position: absolute; right: 20px; bottom: 2px;
    color: #ffffff;
    font-family: "Marcellus", serif;
    font-size: 8.5px;
    line-height: 10px;
    letter-spacing: 3px;
  }
</style>
</head>
<body>

<section class="card card-front" aria-label="Card front">
  <div class="front-wordmark">CORWELL<br>INSIGHT<br>PARTNERS</div>
  <div class="front-tagline">KEEN MINDS. CLEAR CALLS.</div>
</section>

<section class="card card-back" aria-label="Card back">
  <div class="edge-dot"></div>
  <div class="person-name">Daniel Park <span class="ko">박도현</span></div>
  <div class="person-title">CEO &amp; Founder <span class="ko">대표이사</span></div>

  <div class="back-wordmark">CORWELL<br>INSIGHT<br>PARTNERS</div>

  <div class="company-en">Corwell Insight Partners, Inc.</div>
  <div class="company-ko-row">
    <span class="company-ko">코웰인사이트파트너스(주)</span>
    <span class="company-rule"></span>
  </div>

  <div class="contacts">
    <div class="contact-row">
      <span class="contact-item"><svg viewBox="0 0 10 10"><path d="M1 4h8v5H1z M0.5 2.5Q5 0 9.5 2.5V4H0.5z"/></svg>+82 2 718 4052</span>
      <span class="contact-item"><svg viewBox="0 0 10 10"><path d="M3 1h4v3H3z M1 4h8v4H1z M3 7h4v3H3z"/></svg>+82 2 864 1097</span>
      <span class="contact-item"><svg viewBox="0 0 10 10"><path d="M3 0h4a1 1 0 0 1 1 1v8a1 1 0 0 1-1 1H3a1 1 0 0 1-1-1V1a1 1 0 0 1 1-1zm0 1.5v6h4v-6z"/></svg>+82 10 7264 8815</span>
    </div>
    <div class="contact-row">
      <span class="contact-item"><svg viewBox="0 0 10 10"><path d="M0 2h10v6H0z" fill="none" stroke="#1b2656" stroke-width="1.2"/><path d="M0 2l5 4 5-4" fill="none" stroke="#1b2656" stroke-width="1.2"/></svg>daniel@corwellip.com</span>
      <span class="contact-item"><svg viewBox="0 0 10 10"><circle cx="5" cy="5" r="4.3" fill="none" stroke="#1b2656" stroke-width="1.1"/><path d="M0.7 5h8.6M5 0.7c-2.5 2.5-2.5 6.1 0 8.6M5 0.7c2.5 2.5 2.5 6.1 0 8.6" fill="none" stroke="#1b2656" stroke-width=".9"/></svg>www.corwellip.com</span>
    </div>
  </div>

  <div class="address">#507, Hanbit Bldg, 82 Maebongsan-ro, Dobong-gu, Seoul</div>
  <div class="address-ko">서울시 도봉구 매봉산로 82 한빛빌딩 507호</div>

  <svg class="footer-band" viewBox="0 0 484 14" preserveAspectRatio="none" aria-hidden="true">
    <rect x="0" y="0" width="240" height="14" fill="var(--band-grey)"/>
    <polygon points="226,14 238,0 484,0 484,14" fill="var(--navy)"/>
  </svg>
  <div class="back-tagline">KEEN MINDS. CLEAR CALLS.</div>
</section>

</body>
</html>
```